GUARANTEED WordPress design needed for a sassy, confident charisma coach!

We need a website design for Mira Haskett's brand new, responsive, Wordpress website.
Mira is a trainer / coach who teaches people how to be more charismatic and runs events, publishes video courses and has an ongoing video blog. Her old website is here: www.mirahaskett-example.co.uk ... but it's now time to have a much better site!
We have a strong idea about the technical components of the website, but we need a designer's eye to create a great style for the site (and provide layered PSD files which our developers will then convert to HTML and CSS).
Mira's brand is sassy, brave, warm and confident. The videos on her existing site give quite a good feel for her personality. We need a clean, stylish and compelling page that isn't too corporate and captures her personality. Every element needs to feel coherent, from fonts and headings to colours and spacing.
The following sites are not exactly what Mira wants (and certainly aren't right in terms of colours) but they give you an idea of the kind of people she is competing against and the area she is operating in:
http://www.fenna-troske.example/
http://brynwellow.example/
Ideally, you will have done something similar and be able to key in on exactly the kind of thing we want: we're not looking to reinvent the wheel. Hopefully you won't mind tweaking a few things if you are close to what we need.
More detail is provided in the word document attached. But in a nutshell we need: a banner, footer, sign-up strap, menu bar, signature and 4 different basic page types. We want bursts of bright colours, contrasted with black and white if possible - sorry we can't be more specific than that...
The word doc also contains some amateur mock-ups as well (the images are also just mockups at this stage) - but although these give a general sense of the structure what we are looking for, we are clearly not designers...so please help! We need a designer's touch!
Kind regards,
Tomas
PS The layered PSD versions of the mockup files are available on Quellbox: https://files.quellbox.example/sh/k27rpw4m1xqzv/QWxnEr8tLpVu3YcMd0aHs?dl=0
Project Deadline Extended Reason: We are looking for a polished, "designed" look. The mock-up that we have provided is just indicative of the features we want. Added Saturday, May 14, 2016
Entrepreneurs who need to sell themselves.
4 page

```html
<!DOCTYPE html>
<html lang="en">
<head>
<meta charset="utf-8">
<title>Mira Haskett – Charisma Coach</title>
<link href="https://fonts.googleapis.com/css2?family=Open+Sans:wght@300;400;600;700;800&display=swap" rel="stylesheet">
<style>
:root{
  --orange:#f0532d;
  --cyan:#4dd8f2;
  --chat-blue:#1da0e0;
  --yellow:#f7b515;
  --blue:#1a9ee0;
  --magenta:#e2145a;
  --ink:#1e1e1e;
  --text:#555;
  --muted:#8a8a8a;
  --page:#f1f1f1;
  --bar:#ececec;
  --white:#fff;
  --line:#e4e4e4;
}
*{box-sizing:border-box;margin:0;padding:0}
html,body{width:1200px;height:2853px;overflow:hidden}
body{position:relative;background:var(--page);font-family:"Open Sans",Arial,sans-serif;color:var(--ink)}
.abs{position:absolute}

/* top bar */
.topbar{left:0;top:0;width:1200px;height:57px;background:var(--bar)}
.brand{left:224px;top:12px;font-size:24px;font-weight:700;color:var(--ink)}
.menu{left:530px;top:21px;display:flex;list-style:none;font-size:12px;font-weight:600;letter-spacing:.3px}
.menu li{margin-right:50px}
.menu li:last-child{margin-right:0}

/* hero */
.hero{left:0;top:57px;width:1200px;height:371px;background:var(--white)}
.hero-title{right:635px;top:88px;text-align:right;font-size:40px;line-height:52px;font-weight:400;color:#111}
.hero-photo{left:618px;top:0;width:295px;height:371px;background:linear-gradient(180deg,#f4f1ee 0%,#e8cfc9 45%,#d94a3d 70%,#eeeeee 100%)}
.arrow{width:46px;height:46px;border-radius:50%;top:160px;display:flex;align-items:center;justify-content:center}
.arrow.prev{left:91px;background:#e2e2e2}
.arrow.next{left:1048px;background:var(--cyan)}

/* sign-up strap */
.strap{left:0;top:428px;width:1200px;height:247px;background:var(--cyan)}
.laptop-screen{left:281px;top:28px;width:324px;height:232px;border-radius:10px 10px 0 0;background:#1f1f1f;padding:12px 12px 0}
.laptop-screen .display{width:100%;height:100%;background:linear-gradient(180deg,#e9edf2 0%,#c8d3de 60%,#3a69a8 100%)}
.laptop-base{left:224px;top:260px;width:428px;height:18px;border-radius:0 0 14px 14px;background:linear-gradient(180deg,#e4e4e4 0%,#bdbdbd 100%)}
.strap-copy{left:650px;top:30px;width:360px;font-size:19px;line-height:26px;color:#111}
.field{height:34px;background:var(--white);display:flex;align-items:center;padding-left:12px;font-size:10px;color:#333;gap:6px}
.strap .name{left:650px;top:139px;width:155px}
.strap .email{left:812px;top:139px;width:154px}
.yes{width:62px;height:62px;border-radius:50%;background:var(--orange);color:var(--white);font-size:10px;font-weight:700;text-align:center;display:flex;align-items:center;justify-content:center;line-height:13px;border:3px solid #ff8a6b}
.strap .yes{left:973px;top:127px}
.strap-note{left:650px;top:187px;font-size:8px;color:#222}

/* posts */
.post{left:224px;width:468px;height:418px;background:var(--white)}
.post h2{position:absolute;left:26px;top:22px;font-size:15px;font-weight:400;color:#111}
.post .banner{position:absolute;left:26px;top:57px;width:417px;height:209px;overflow:hidden}
.post p{position:absolute;left:26px;top:282px;width:417px;font-size:9.5px;line-height:17px;color:var(--text)}
.btn{background:var(--orange);color:var(--white);font-size:9px;font-weight:700;letter-spacing:.3px;display:inline-flex;align-items:center;justify-content:center;gap:6px}
.post .btn{position:absolute;left:26px;top:372px;width:106px;height:24px}
.banner .shot{position:absolute;right:0;top:0;height:100%}
.banner .b-text{position:absolute;left:32px;color:var(--white)}
.banner .b-btn{position:absolute;left:32px;font-size:10px;font-weight:700;padding:8px 14px}
.play{position:absolute;width:48px;height:48px;border-radius:50%;background:rgba(255,255,255,.75);display:flex;align-items:center;justify-content:center}

/* pagination */
.pager{left:460px;top:2520px;display:flex}
.pager span{width:33px;height:30px;display:flex;align-items:center;justify-content:center;font-size:10px;color:var(--white);background:#3a3a3a;border-right:1px solid #2c2c2c}
.pager .edge{background:#555}
.pager .on{background:var(--orange)}

/* sidebar */
.panel{left:713px;width:261px;background:var(--white)}
.panel-title{font-size:14px;color:var(--orange)}
.says{top:736px;height:371px;padding:10px 18px}
.says .panel-title b{font-weight:700}
.tab{margin:14px 0 10px 80px;width:62px;height:20px;border:1px solid var(--cyan);color:var(--cyan);font-size:8px;font-weight:700;display:flex;align-items:center;justify-content:center}
.says ul{list-style:none}
.says li{position:relative;padding:6px 0 10px 24px;border-bottom:1px solid var(--line);margin-bottom:8px}
.says li:last-child{border-bottom:0}
.says li::before{content:"";position:absolute;left:2px;top:8px;width:10px;height:8px;background:#d6d6d6}
.says .t{font-size:9.5px;line-height:15px;color:#222}
.date{display:inline-block;margin-top:6px;padding:3px 8px;background:#e9e9e9;font-size:7px;color:#444}

.coming-title{left:713px;top:1126px}
.event{left:713px;top:1156px;width:261px;height:371px;overflow:hidden;background:linear-gradient(180deg,#c9c2b8 0%,#8e8a84 50%,#4d4a47 100%)}
.event svg{position:absolute;left:0;top:0}
.event .ev-text{position:absolute;left:18px;top:218px;color:var(--white);line-height:27px}
.event .ev-text .live,.event .ev-text .big{font-size:22px;font-weight:700}
.event .ev-text .sub{font-size:22px;font-weight:400}
.event .btn{position:absolute;left:18px;top:338px;width:86px;height:24px}

.tweets{top:1554px;height:367px;padding:6px 18px}
.tweets .panel-title{font-size:12px;color:var(--chat-blue)}
.tw-frame{margin-top:8px;border:1px solid #d8d8d8;height:315px;position:relative}
.tw-head{height:24px;background:var(--chat-blue);color:var(--white);font-size:9px;display:flex;align-items:center;justify-content:space-between;padding:0 8px}
.tw-head i{width:12px;height:12px;background:var(--white);display:block}
.tw-item{display:flex;gap:10px;padding:10px 10px 6px;font-size:9px;line-height:14px;color:#333}
.tw-item .av{flex:none;width:24px;height:24px;background:#777}
.tw-item a{color:var(--chat-blue);text-decoration:none}
.tw-item small{display:block;color:var(--muted);font-size:8px}
.tw-foot{position:absolute;left:0;bottom:0;width:100%;height:28px;background:var(--chat-blue);color:var(--white);font-size:8px;display:flex;align-items:center;justify-content:space-between;padding:0 10px}

.stories{top:1940px;height:371px;padding:10px 18px}
.story{display:flex;gap:14px;margin-top:18px}
.story .ph{flex:none;width:56px;height:56px;border-radius:50%;background:linear-gradient(135deg,#b7a79d,#5c4f49)}
.story p{font-size:9px;line-height:15px;color:#444}
.story .who{display:inline-block;margin-top:8px;padding:3px 10px;background:#e9e9e9;font-size:7px;color:#444}
.stories .btn{position:absolute;right:10px;bottom:14px;width:124px;height:22px;font-size:8px}

/* footer */
.footer{left:0;top:2583px;width:1200px;height:270px;background:var(--bar);text-align:center}
.footer-copy{position:absolute;left:0;width:1200px;top:30px;font-size:12.5px;line-height:23px;color:#222}
.footer .name{left:406px;top:99px;width:157px}
.footer .email{left:570px;top:99px;width:155px}
.footer .yes{left:731px;top:84px}
.footer-note{position:absolute;left:0;width:1200px;top:158px;font-size:9px;color:#222}
.social{left:523px;top:183px;display:flex;gap:6px}
.social span{width:24px;height:24px;display:block}
.legal{left:0;width:1200px;top:232px;display:flex;justify-content:center;gap:30px;font-size:7.5px;font-weight:600;color:#222}
</style>
</head>
<body>

<header class="abs topbar">
  <div class="abs brand">Mira Haskett</div>
  <ul class="abs menu">
    <li>EVENTS</li><li>WORK WITH ME</li><li>CORPORATE</li><li>ABOUT</li><li>CONTACT</li>
  </ul>
</header>

<section class="abs hero">
  <h1 class="abs hero-title">ATTRACT<br>CONNECT<br>INFLUENCE</h1>
  <div class="abs hero-photo" role="img" aria-label="Photo of Mira in a red dress seated on a white egg chair"></div>
  <div class="abs arrow prev"><svg width="12" height="12" viewBox="0 0 12 12"><path d="M8 1 3 6l5 5" fill="none" stroke="#777" stroke-width="1.6"/></svg></div>
  <div class="abs arrow next"><svg width="12" height="12" viewBox="0 0 12 12"><path d="M4 1l5 5-5 5" fill="none" stroke="#fff" stroke-width="1.6"/></svg></div>
</section>

<section class="abs strap">
  <div class="abs laptop-screen"><div class="display" role="img" aria-label="Free training video of Mira playing on a laptop"></div></div>
  <div class="abs laptop-base"></div>
  <p class="abs strap-copy">Learn how to unlock the superpower* of your charisma and win all the business you want with this FREE training.</p>
  <div class="abs field name">&#9679; Name</div>
  <div class="abs field email">&#9993; E mail</div>
  <div class="abs yes">YES<br>PLEASE!</div>
  <p class="abs strap-note">* Promise to only use your powers for good</p>
</section>

<article class="abs post" style="top:736px">
  <h2>Public speaking... made easy</h2>
  <div class="banner" style="background:#5d5d5d">
    <div class="shot" role="img" aria-label="Photo of Mira speaking on stage in a red jacket" style="left:230px;background:linear-gradient(180deg,#6a6a6a,#8b3a33)"></div>
    <div class="b-text" style="top:52px;font-size:22px;line-height:29px">PUBLIC<br><b style="font-weight:800">SPEAKING...</b><br><span style="color:#9a9a9a">Made Easy :)</span></div>
    <div class="play" style="left:172px;top:72px"><svg width="16" height="18" viewBox="0 0 16 18"><path d="M2 1l13 8-13 8z" fill="#5d5d5d"/></svg></div>
  </div>
  <p>Sed ut perspiciatis unde omnis iste natus error sit voluptatem accusantium doloremque laudantium, totam rem aperiam, eaque ipsa quae ab illo inventore veritatis et quasi architecto beatae vitae dicta sunt explicabo. Nemo enim ipsam voluptatem quia voluptas sit aspernatur aut odit aut fugit sed quia consequuntur magni dolores eos.</p>
  <span class="btn">KEEP READING &#10230;</span>
</article>

<article class="abs post" style="top:1183px">
  <h2>Unfulfilled? It's time to think about your values...</h2>
  <div class="banner" style="background:var(--yellow)">
    <div class="shot" role="img" aria-label="Photo of Mira gesturing while explaining" style="left:270px;background:linear-gradient(180deg,#f7b515,#8a6a4a)"></div>
    <div class="b-text" style="top:30px;font-size:21px;line-height:30px"><b style="font-weight:800">Unfulfilled?</b> It's Time<br>to think About your<br>Values...</div>
    <div class="play" style="left:178px;top:70px"><svg width="16" height="18" viewBox="0 0 16 18"><path d="M2 1l13 8-13 8z" fill="#f7b515"/></svg></div>
    <span class="b-btn" style="top:140px;background:#ffe23a;color:#222">DO THIS EXERCISE NOW!</span>
  </div>
  <p>But I must explain to you how all this mistaken idea of denouncing pleasure and praising pain was born and I will give you a complete account of the system, and expound the actual teachings of the great explorer of the truth, the master-builder of human happiness. No one rejects, dislikes, or avoids pleasure itself, because...</p>
  <span class="btn">KEEP READING &#10230;</span>
</article>

<article class="abs post" style="top:1630px">
  <h2>How to start every day in the right frame of mind!</h2>
  <div class="banner" style="background:var(--blue)">
    <div class="shot" role="img" aria-label="Portrait of Mira smiling in glasses" style="left:255px;background:linear-gradient(180deg,#1a9ee0,#3b3aa8)"></div>
    <div class="b-text" style="top:30px;font-size:21px;line-height:30px">How to start every<br>day In the right<br><b style="font-weight:800">frame Of mind!</b></div>
    <span class="b-btn" style="top:140px;background:#0d6fb8;color:#fff">DO THIS EXERCISE NOW!</span>
  </div>
  <p>But I must explain to you how all this mistaken idea of denouncing pleasure and praising pain was born and I will give you a complete account of the system, and expound the actual teachings of the great explorer of the truth, the master-builder of human happiness. No one rejects, dislikes, or avoids pleasure itself, because...</p>
  <span class="btn">KEEP READING &#10230;</span>
</article>

<article class="abs post" style="top:2079px">
  <h2>How to start every day in the right frame of mind!</h2>
  <div class="banner" style="background:var(--magenta)">
    <div class="shot" role="img" aria-label="Style tips board with a red dress and Mira in glasses" style="left:222px;background:linear-gradient(180deg,#f4f4f4 0%,#f4f4f4 60%,#8a3a4a 100%)"></div>
    <div class="b-text" style="top:30px;font-size:21px;line-height:26px">TAKE CHARGE OF<br>YOUR STYLE...<br><b style="font-weight:800;font-size:17px">...BOOST YOUR<br>CONFIDENCE</b></div>
    <span class="b-btn" style="top:140px;background:#b80d47;color:#fff">DO THIS EXERCISE NOW!</span>
  </div>
  <p>But I must explain to you how all this mistaken idea of denouncing pleasure and praising pain was born and I will give you a complete account of the system, and expound the actual teachings of the great explorer of the truth, the master-builder of human happiness. No one rejects, dislikes, or avoids pleasure itself, because...</p>
  <span class="btn">KEEP READING &#10230;</span>
</article>

<nav class="abs pager">
  <span class="edge">&lsaquo;</span><span class="on">1</span><span>2</span><span>3</span><span>4</span><span>5</span><span class="edge">&rsaquo;</span>
</nav>

<aside class="abs panel says">
  <h3 class="panel-title"><b>Mira</b> Says</h3>
  <div class="tab">POPULAR</div>
  <ul>
    <li><div class="t">Be more dog: 5 lessons we could learn from our best friends</div><span class="date">July 17, 2015</span></li>
    <li><div class="t">Are you letting your core beliefs hold you back?</div><span class="date">July 17, 2015</span></li>
    <li><div class="t">How I learned to stop worrying and start NETWORKING!</div><span class="date">July 17, 2015</span></li>
    <li><div class="t">Bitchy resting face and other strange - but true - problems.</div><span class="date">July 17, 2015</span></li>
  </ul>
</aside>

<h3 class="abs panel-title coming-title">Coming Up</h3>
<div class="abs event">
  <div role="img" aria-label="Photo of a live workshop audience in a loft venue" style="position:absolute;inset:0"></div>
  <svg width="261" height="371" viewBox="0 0 261 371"><path d="M0 371V150L175 40v331z" fill="#4dd8f2" opacity=".88"/></svg>
  <div class="ev-text"><div class="live">LIVE</div><div class="big">Unlock</div><div class="sub">The Superpower<br>Of charisma</div></div>
  <span class="btn">LEARN MORE</span>
</div>

<aside class="abs panel tweets">
  <h3 class="panel-title">Tweets</h3>
  <div class="tw-frame">
    <div class="tw-head">Chatter <i></i></div>
    <div class="tw-item"><span class="av"></span><div><a>@Rowan</a> belief, Lorem Ipsum is not simply <a>random text.</a><small>43 minutes ago</small></div></div>
    <div class="tw-item"><span class="av"></span><div><a>@Wren</a> established fact that a reader will be distracted by the<small>43 minutes ago</small></div></div>
    <div class="tw-item"><span class="av"></span><div><a>@Fenwick</a> many variations of passages of Lorem Ipsum<small>43 minutes ago</small></div></div>
    <div class="tw-item"><span class="av"></span><div><a>@Milo</a> chunk of Lorem Ipsum <a>used since</a><small>1 hour ago</small></div></div>
    <div class="tw-foot"><span>Chatter</span><span>Join the Conversation</span></div>
  </div>
</aside>

<aside class="abs panel stories">
  <h3 class="panel-title"><b>Success</b> Stories</h3>
  <div class="story"><span class="ph" role="img" aria-label="Client portrait"></span><div><p>I've never been a fashionista and my wardrobe was dominated by the colour black... my appearance in terms of make-up and clothing had become dull and uninteresting. One day with Mira and I was transformed!</p><span class="who">Marie - HR Director</span></div></div>
  <div class="story"><span class="ph" role="img" aria-label="Client portrait"></span><div><p>I visited Mira for a 1 to 1 impact session. I've recently set up my own business and wanted to ensure that I was giving off the perfect image for the role into which I was stepping. The session was fantastic...</p><span class="who">Emily - Director</span></div></div>
  <span class="btn">READ FULL TESTIMONIALS</span>
</aside>

<footer class="abs footer">
  <p class="footer-copy">Hey! Don't go without signing up because you'll miss out on exclusive offers, awesome tips,<br>and weekly motivation in my fab newsletter *.</p>
  <div class="abs field name">&#9679; Name</div>
  <div class="abs field email">&#9993; E mail</div>
  <div class="abs yes">YES<br>PLEASE!</div>
  <p class="footer-note">* And that'll make me sad :(</p>
  <div class="abs social">
    <span style="background:#35a9e0" aria-label="social link"></span>
    <span style="background:#3b5a98" aria-label="social link"></span>
    <span style="background:#1b77b4" aria-label="social link"></span>
    <span style="background:#c8232c" aria-label="social link"></span>
    <span style="background:#b57a4c" aria-label="social link"></span>
  </div>
  <div class="abs legal"><span>© 2016 Mira Haskett Ltd</span><span>PRIVACY POLICY</span><span>TERMS POLICY</span><span>DISCLAIMERS</span></div>
</footer>

</body>
</html>
```